Women's Health Company needs business card

We need a business card for a USA based women's health care company. We use digital technology to enhance therapy prescribed by clinicians for their patients

```html
<!DOCTYPE html>
<html lang="en">
<head>
<meta charset="utf-8">
<title>Lunara Health – Business Card</title>
<link rel="stylesheet" href="https://fonts.googleapis.com/css2?family=Montserrat:wght@400;500;800&display=swap">
<style>
  :root {
    --backdrop: #252525;
    --purple: #9355a0;
    --teal: #78bfbf;
    --white: #ffffff;
    --ink: #1f1f1f;
  }
  * { margin: 0; padding: 0; box-sizing: border-box; }
  html, body {
    width: 1200px; height: 900px; overflow: hidden;
    background: var(--backdrop);
    font-family: "Montserrat", sans-serif;
  }
  .canvas { position: relative; width: 1200px; height: 900px; }

  .card {
    position: absolute; left: 250px; width: 700px; height: 400px;
    overflow: hidden;
  }
  .card--front { top: 30px; background: var(--purple); }
  .card--back  { top: 470px; background: var(--white); }

  .brand {
    position: absolute; display: flex; align-items: center; gap: 14px;
    font-weight: 500; white-space: nowrap; letter-spacing: 1px;
  }
  .brand__dot { border-radius: 50%; flex: none; }

  .card--front .brand {
    left: 0; right: 0; top: 160px; justify-content: center;
    font-size: 64px; color: var(--white);
  }
  .card--front .brand__dot { width: 16px; height: 16px; background: var(--white); }

  .card__band { position: absolute; left: 0; top: 0; }

  .card__footer {
    position: absolute; left: 0; right: 0; bottom: 0; height: 22px;
    background: var(--purple);
  }

  .card--back .brand {
    right: 48px; top: 212px; font-size: 32px; color: var(--teal); gap: 10px;
  }
  .card--back .brand__dot { width: 10px; height: 10px; background: var(--teal); }

  .person { position: absolute; left: 48px; top: 170px; }
  .person__name {
    font-weight: 800; font-size: 27px; color: var(--purple); letter-spacing: 0.5px;
  }
  .person__role { font-size: 17px; color: var(--ink); margin-top: 2px; }

  .contact {
    position: absolute; left: 40px; top: 250px; list-style: none;
  }
  .contact__item {
    display: flex; align-items: center; gap: 12px;
    font-size: 17px; color: var(--ink); height: 30px;
  }
  .contact__icon { width: 18px; height: 18px; flex: none; fill: var(--purple); }

  .address {
    position: absolute; right: 48px; top: 300px; text-align: left;
    font-size: 17px; line-height: 1.35; color: var(--ink); font-weight: 500;
  }
</style>
</head>
<body>
<main class="canvas">

  <section class="card card--front" aria-label="Card front">
    <div class="brand"><span class="brand__dot"></span>Lunara Health</div>
  </section>

  <section class="card card--back" aria-label="Card back">
    <svg class="card__band" viewBox="0 0 700 140" width="700" height="140" aria-hidden="true">
      <path fill="var(--purple)" d="M0 0 H700 V110 C520 140 200 140 0 100 Z"/>
    </svg>

    <div class="person">
      <div class="person__name">MARISOL</div>
      <div class="person__role">Co-Founder</div>
    </div>

    <ul class="contact">
      <li class="contact__item">
        <svg class="contact__icon" viewBox="0 0 24 24" aria-hidden="true"><path d="M6.6 10.8a15.1 15.1 0 0 0 6.6 6.6l2.2-2.2a1 1 0 0 1 1-.25 11.4 11.4 0 0 0 3.6.57 1 1 0 0 1 1 1V20a1 1 0 0 1-1 1A17 17 0 0 1 3 4a1 1 0 0 1 1-1h3.5a1 1 0 0 1 1 1c0 1.25.2 2.45.57 3.57a1 1 0 0 1-.25 1z"/></svg>
        555-201-3348
      </li>
      <li class="contact__item">
        <svg class="contact__icon" viewBox="0 0 24 24" aria-hidden="true"><path d="M2 5h20v14H2z M4 7v.5l8 5 8-5V7l-8 5z" fill-rule="evenodd"/></svg>
        hello@lunaracare.net
      </li>
      <li class="contact__item">
        <svg class="contact__icon" viewBox="0 0 24 24" aria-hidden="true"><circle cx="12" cy="12" r="10"/><path d="M2 12h20M12 2c3 3 3 17 0 20M12 2c-3 3-3 17 0 20" stroke="var(--white)" stroke-width="1.4" fill="none"/></svg>
        www.lunaracare.net
      </li>
    </ul>

    <div class="brand"><span class="brand__dot"></span>Lunara Health</div>

    <p class="address">Brightline Plaza 2200 Meadow<br>Crest Ave Suite 310</p>

    <div class="card__footer"></div>
  </section>

</main>
</body>
</html>
```